Hello , we need a 1 page A4 flyer. the flyer needs a heading and then 4 sub headings and catagoring. The words on the attached example are the same length as our text. we are open to a new modern look and the information can be in 1 or 2 coloums. we are an australian law firm and I have also attachd our logo. the bottom 1/4 of the page is a graphic you need to allow space for. we have blue as a corporate colour and do not have a font or style. please use the 5 headings and we will complete the words / text afterwards so we will need the final version to be a word document. for assistance see www.jurapath-example.com.au
Legal

```html
<!DOCTYPE html>
<html lang="en">
<head>
<meta charset="utf-8">
<title>JuraPath – Who is JuraPath?</title>
<link href="https://fonts.googleapis.com/css2?family=Arimo:wght@400;700&display=swap" rel="stylesheet">
<style>
  :root {
    --backdrop: #d9d9d9;
    --paper: #ffffff;
    --brand-blue: #1f5fae;
    --brand-cyan: #1c9cc8;
    --body-grey: #9b9b9b;
    --statement-grey: #7d7d7d;
    --band-light: #1b8fb6;
    --band-dark: #15708f;
  }
  * { margin: 0; padding: 0; box-sizing: border-box; }
  html, body {
    width: 1200px; height: 960px; overflow: hidden;
    background: var(--backdrop);
    font-family: "Arimo", Arial, sans-serif;
  }
  .flyer {
    position: absolute; left: 282px; top: 30px;
    width: 636px; height: 900px;
    background: var(--paper);
    box-shadow: 0 4px 18px rgba(0,0,0,0.18);
    overflow: hidden;
  }
  .brand {
    position: absolute; left: 56px; top: 48px;
    display: flex; align-items: center; gap: 10px;
  }
  .brand-square { width: 34px; height: 34px; background: var(--brand-cyan); }
  .brand-name { font-size: 26px; font-weight: 400; color: var(--brand-blue); line-height: 1; }
  .brand-tagline { font-size: 10.5px; color: var(--brand-cyan); margin-top: 4px; letter-spacing: 0.3px; }
  .intro { position: absolute; left: 56px; top: 148px; width: 524px; }
  .intro-title { font-size: 38px; font-weight: 400; color: var(--brand-blue); line-height: 1.1; }
  .intro-statement {
    margin-top: 10px; font-size: 15px; font-weight: 700;
    color: var(--statement-grey); line-height: 1.3;
  }
  .columns {
    position: absolute; left: 56px; top: 298px; width: 524px;
    display: grid; grid-template-columns: 1fr 1fr; column-gap: 36px;
  }
  .section { margin-bottom: 20px; }
  .section-head { display: flex; align-items: flex-start; gap: 8px; }
  .section-marker { flex: none; width: 11px; height: 11px; margin-top: 3px; background: var(--brand-blue); }
  .section-title { font-size: 14.5px; font-weight: 700; color: var(--brand-cyan); line-height: 1.2; }
  .section-body p {
    margin-top: 8px; padding-left: 19px;
    font-size: 9.5px; color: var(--body-grey); line-height: 1.4;
  }
  .graphic-space {
    position: absolute; left: 0; bottom: 0; width: 100%; height: 222px;
    background: linear-gradient(135deg, var(--band-light) 0%, var(--band-dark) 100%);
  }
</style>
</head>
<body>
  <main class="flyer">
    <header class="brand">
      <span class="brand-square"></span>
      <div>
        <div class="brand-name">JuraPath</div>
        <div class="brand-tagline">strategic legal outsourcing</div>
      </div>
    </header>

    <section class="intro">
      <h1 class="intro-title">Who is JuraPath?</h1>
      <p class="intro-statement">This is a statement header small paragraph. This is a statement header small paragraph. This is a statement header small paragraph. This is a statement header small paragraph</p>
    </section>

    <div class="columns">
      <div class="column">
        <article class="section">
          <div class="section-head"><span class="section-marker"></span><h2 class="section-title">Next generation legal<br>and lender process services</h2></div>
          <div class="section-body">
            <p>Paragraph 1. Paragraph 1. Paragraph 1. Paragraph 1. Paragraph 1. Paragraph 1. Paragraph 1. Paragraph 1. Paragraph 1. Paragraph 1. Paragraph 1. Paragraph 1. Paragraph 1. Paragraph 1. Paragraph 1.</p>
            <p>Paragraph 2. Paragraph 2. Paragraph 2. Paragraph 2. Paragraph 2. Paragraph 2. Paragraph 2. Paragraph 2. Paragraph 2. Paragraph 2. Paragraph 2. Paragraph 2. Paragraph 2. Paragraph 2. Paragraph 2. Paragraph 2.</p>
          </div>
        </article>
        <article class="section">
          <div class="section-head"><span class="section-marker"></span><h2 class="section-title">How you will benefit from us</h2></div>
          <div class="section-body">
            <p>Paragraph 1. Paragraph 1. Paragraph 1. Paragraph 1. Paragraph 1. Paragraph 1. Paragraph 1. Paragraph 1. Paragraph 1. Paragraph 1. Paragraph 1. Paragraph 1. Paragraph 1. Paragraph 1. Paragraph 1. Paragraph 1. Paragraph 1. Paragraph 1. Paragraph 1. Paragraph 1. Paragraph 1. Paragraph 1. Paragraph 1. Paragraph 1. Paragraph 1. Paragraph 1.</p>
          </div>
        </article>
      </div>
      <div class="column">
        <article class="section">
          <div class="section-head"><span class="section-marker"></span><h2 class="section-title">We understand the importance of the work we do for you</h2></div>
          <div class="section-body">
            <p>Paragraph 1. Paragraph 1. Paragraph 1. Paragraph 1. Paragraph 1. Paragraph 1. Paragraph 1. Paragraph 1. Paragraph 1. Paragraph 1. Paragraph 1. Paragraph 1. Paragraph 1. Paragraph 1. Paragraph 1.</p>
            <p>Paragraph 2. Paragraph 2. Paragraph 2. Paragraph 2. Paragraph 2. Paragraph 2. Paragraph 2. Paragraph 2. Paragraph 2. Paragraph 2. Paragraph 2.</p>
          </div>
        </article>
        <article class="section">
          <div class="section-head"><span class="section-marker"></span><h2 class="section-title">Results, not just promises</h2></div>
          <div class="section-body">
            <p>Paragraph 1. Paragraph 1. Paragraph 1. Paragraph 1. Paragraph 1. Paragraph 1. Paragraph 1. Paragraph 1. Paragraph 2. Paragraph 2. Paragraph 2. Paragraph 2. Paragraph 2. Paragraph 2. Paragraph 2. Paragraph 2.</p>
          </div>
        </article>
      </div>
    </div>

    <div class="graphic-space" role="img" aria-label="Reserved area for the corporate blue stream graphic"></div>
  </main>
</body>
</html>
```